Brochure Design Project for Building Designer

I need a modern and edgy brochure to introduce my new business TORV Design, Commercial and Residential Building Designers.

We specialise in Building Design, Project Management and Design Consultation.

I would like the brochure to be anywhere between 2-4 pages, depending of amount of suitable content available.
Colours to be black and white with splashes of
bright colours (mostly incorporated in photos).

Main Content of brochure to be broken up into 3 (maybe 4) sections to include:

About Us
Services
Projects

Logo Text (DESIGN etc) can be changed to white if suits better with black background.

Would be nice to include sketches to give it that architectural feel.

Samples and wording will be uploaded shortly
Updates

I HAVE PROVIDED A COMPLETE UPDATE OF PROJECT REQUIREMENTS INCLUDING ALL NEW UPLOADED FILES.

PLEASE REFER TO THE BROCHURE LAYOUT PDF UPLOADEDĀ FOR FULL INFORMATION ON PROJECT INCLUDING BROCHURE LAYOUT.

IF YOU HAVE ANY QUESTIONS OR REQUIRE ANY FURTHER INFORMATION, PLEASE LET ME KNOW

I HAVE ADDED FURTHER DEVELOPED PDF DOCUMENTS OF BROCHURE.

IF YOU HAVE TROUBLE OPENING THESE DOCS IN ADOBE ILLUSTRATOR THRU ADOBE BRIDGE PLEASE LET ME KNOW & I WILL UPLOAD AI FILES.

CAN YOU PLEASE FINE TUNE GRAPHICS AND WORK ON BACKGROUND

Target Market(s)

Builders, Property Developers, Architects, Consultants, Professionals

Industry/Entity Type

Business

Requirements
Must have
• Very Professional Look
Black and White
Simple and easy to read layout
Either A4 (if only 2 pages) or
A3 double sided with centre fold (if 4 pages)
Touch up of photos (if possible) to make them stand out of the page.
Samples of recent projects with photos
Should not have
• Any comics or similar

```html
<!DOCTYPE html>
<html lang="en">
<head>
<meta charset="utf-8">
<title>TORV Design – About Us &amp; Services</title>
<link rel="stylesheet" href="https://fonts.googleapis.com/css2?family=Didact+Gothic&family=Kaushan+Script&family=Arimo&display=swap">
<style>
  :root {
    --page-bg: #ffffff;
    --panel-light: #eceef2;
    --panel-mid: #e3e4e9;
    --panel-deep: #dadbe1;
    --heading: #5a3c1c;
    --body-text: #1e1e1e;
    --accent-pink: #e8409a;
    --photo-ceiling: #f0e4cf;
    --photo-wall: #dcc29a;
    --photo-warm: #c7a676;
    --photo-table: #4a3a2e;
    --photo-floor: #dccfb9;
    --photo-name: rgba(255, 255, 255, 0.8);
  }
  * { margin: 0; padding: 0; box-sizing: border-box; }
  html, body {
    width: 1200px;
    height: 1000px;
    overflow: hidden;
    background: var(--page-bg);
  }
  .canvas {
    position: relative;
    width: 1200px;
    height: 1000px;
    font-family: "Didact Gothic", "Century Gothic", sans-serif;
    color: var(--body-text);
  }
  .panel {
    position: absolute;
    left: 52px;
    top: 60px;
    width: 1095px;
    height: 878px;
    background: linear-gradient(135deg, var(--panel-light) 0%, var(--panel-mid) 50%, var(--panel-deep) 100%);
  }
  .interior-photo {
    position: absolute;
    left: 52px;
    top: 60px;
    width: 442px;
    height: 791px;
    background:
      linear-gradient(180deg,
        var(--photo-ceiling) 0%,
        var(--photo-wall) 30%,
        var(--photo-warm) 55%,
        #8f7558 68%,
        var(--photo-table) 78%,
        #9c8a74 88%,
        var(--photo-floor) 100%);
  }
  .photo-name {
    position: absolute;
    left: 58px;
    top: 800px;
    font-size: 40px;
    letter-spacing: 4px;
    color: var(--photo-name);
  }
  .section-heading {
    position: absolute;
    left: 511px;
    font-size: 24px;
    font-weight: 400;
    color: var(--heading);
  }
  .about-heading { top: 78px; }
  .services-heading { top: 554px; }
  .body-copy {
    position: absolute;
    left: 511px;
    font-size: 17.8px;
    line-height: 24px;
  }
  .about-intro { top: 118px; width: 610px; }
  .experience-list {
    position: absolute;
    top: 171px;
    list-style: none;
    font-size: 17.8px;
    line-height: 24.3px;
  }
  .experience-list li { position: relative; padding-left: 26px; }
  .experience-list li::before {
    content: "";
    position: absolute;
    left: 2px;
    top: 10px;
    width: 6px;
    height: 6px;
    border-radius: 50%;
    background: var(--body-text);
  }
  .list-left { left: 511px; }
  .list-right { left: 838px; width: 290px; }
  .quote {
    position: absolute;
    left: 560px;
    width: 556px;
    text-align: center;
    font-family: "Kaushan Script", cursive;
    color: var(--accent-pink);
  }
  .quote-text { top: 310px; font-size: 41px; line-height: 58px; }
  .quote-author { top: 430px; font-size: 25px; }
  .efficiency-note { top: 483px; width: 610px; }
  .services-intro { top: 592px; }
  .services-list {
    position: absolute;
    left: 511px;
    top: 616px;
    list-style: none;
    font-size: 17.8px;
    line-height: 24.2px;
  }
  .drafting-note {
    position: absolute;
    left: 73px;
    top: 874px;
    width: 1060px;
    font-family: "Arimo", Arial, sans-serif;
    font-size: 16.5px;
    line-height: 23px;
    color: #111;
  }
</style>
</head>
<body>
<div class="canvas">
  <div class="panel" role="img" aria-label="Pale grey background with faint architectural line sketch"></div>

  <div class="interior-photo" role="img" aria-label="Photograph of a double-height residential interior with a floating staircase, lounge and black glass dining table"></div>
  <div class="photo-name">TORV</div>

  <h2 class="section-heading about-heading">About Us</h2>
  <p class="body-copy about-intro">Torv design has a diverse portfolio of commercial + residential work across a range of scales, budgets + project types. Areas of experience include:</p>
  <ul class="experience-list list-left">
    <li>Commercial developments</li>
    <li>Mixed-use developments</li>
    <li>Residential &amp; multi residential</li>
    <li>Upmarket individual houses</li>
    <li>Healthcare</li>
  </ul>
  <ul class="experience-list list-right">
    <li>Commercial industrial</li>
    <li>Cafes/restaurants</li>
    <li>Alterations + additions</li>
    <li>Residential + commercial interior fitouts</li>
  </ul>

  <p class="quote quote-text">“Simplicity is the ultimate<br>sophistication”</p>
  <p class="quote quote-author">Lorenzo Varelli</p>

  <p class="body-copy efficiency-note">We strive to be efficient at all times in every aspect of our service + pride ourselves on our attention to detail.</p>

  <h2 class="section-heading services-heading">Services</h2>
  <p class="body-copy services-intro">We are able to provide a wide range of services:</p>
  <ul class="services-list">
    <li>Project planning</li>
    <li>Design concepts</li>
    <li>Design development / development approval</li>
    <li>Consultant liaison + management</li>
    <li>Building certification</li>
    <li>Tender / construction documentation</li>
    <li>Project management</li>
    <li>3D modelling &amp; renders</li>
    <li>Re-documentation &amp; design consultation</li>
    <li>Drafting services</li>
  </ul>

  <p class="drafting-note">We offer high quality drafting solutions for pre-designed projects of any size to ensure you get the best quality drawings for local authority + construction issue.</p>
</div>
</body>
</html>
```